Kelvora Energy Brochure

This will be an 8 page brochure 8.5 X 11" Page Order: Front Cover, Solar, Storage, O&M, Automated Cleaning Systems, Electrical, Roofing, Back Cover. Most information needed can be found on our website. Ask for anything you need.

Target Market(s)

Commercial Solar Customers, Roofing Customers

Industry/Entity Type

Renewable Energy

Font styles to use
Serif

Colors
0054AA
0677BA
7BADD7
CADEEF
E8F1F8

```html
<!DOCTYPE html>
<html lang="en">
<head>
<meta charset="utf-8">
<title>Kelvora Energy Brochure</title>
<link href="https://fonts.googleapis.com/css2?family=Noto+Serif:wght@400;700&display=swap" rel="stylesheet">
<style>
:root{
  --navy:#0054AA;
  --blue:#0677BA;
  --sky:#7BADD7;
  --pale:#CADEEF;
  --mist:#E8F1F8;
  --ink:#33404d;
  --bg:#ececec;
}
*{margin:0;padding:0;box-sizing:border-box}
html,body{width:1200px;height:1022px;overflow:hidden;background:var(--bg)}
body{position:relative;font-family:"Noto Serif",Georgia,serif;color:var(--ink)}
.spread{position:absolute;width:580px;height:375px;background:#fff;overflow:hidden;box-shadow:0 1px 3px rgba(0,0,0,.15)}
.spread-cover{left:12px;top:128px}
.spread-solar{left:608px;top:128px}
.spread-om{left:12px;top:519px}
.spread-trades{left:608px;top:519px}
.page{position:absolute;top:0;width:290px;height:375px;overflow:hidden}
.page-left{left:0}
.page-right{left:290px}
.wash{position:absolute;left:0;top:0;width:290px;background:var(--pale)}
.photo{position:absolute}
.tab{position:absolute;background:var(--navy)}
.title{position:absolute;left:15px;top:12px;font-weight:400;font-size:14.5px;line-height:15px;color:var(--blue);text-transform:uppercase;letter-spacing:.2px}
.sub{position:absolute;left:15px;font-size:4.6px;line-height:5.6px;color:var(--ink)}
.col{position:absolute;width:82px}
.col h3{font-weight:400;font-size:6px;line-height:6.6px;color:var(--blue);text-transform:uppercase;margin-bottom:3px}
.col p,.body{font-size:4.2px;line-height:5.2px;color:var(--ink);margin-bottom:3px}
.lead{position:absolute;font-size:5.8px;line-height:7px;color:var(--blue);text-transform:uppercase}
.checks{position:absolute;list-style:none}
.checks li{position:relative;padding-left:8px;font-size:4.2px;line-height:5.2px;margin-bottom:4.4px;color:var(--ink)}
.checks li::before{content:"";position:absolute;left:0;top:0;width:4px;height:2.2px;border-left:1.2px solid var(--blue);border-bottom:1.2px solid var(--blue);transform:rotate(-45deg)}
.checks.wide li{padding-left:12px;margin-bottom:7px}
.checks.wide li::before{width:6px;height:3.2px;border-width:1.6px}
.badge{position:absolute;width:60px;text-align:center;font-size:3.8px;line-height:4.8px;font-weight:700;color:var(--ink);text-transform:uppercase}
.badge i{display:block;width:11px;height:11px;margin:0 auto 4px;border-radius:50%;background:var(--sky);border:2px solid var(--blue)}
.subhead{font-size:5.4px;line-height:6.4px;color:var(--blue);text-transform:uppercase;margin-bottom:3px}
.brand{position:absolute;font-family:"Noto Serif",Georgia,serif;font-weight:700;white-space:nowrap}
.cover-brand-top{left:290px;width:290px;top:18px;text-align:center;font-size:19px;color:var(--navy)}
.cover-brand-band{left:60px;top:236px;font-size:13px;color:#fff}
.cover-headline{position:absolute;left:330px;width:240px;top:93px;text-align:center;color:#fff}
.cover-headline h1{font-weight:400;font-size:14px;line-height:15px}
.cover-headline p{font-size:5px;margin-top:3px}
.contact{position:absolute;left:20px;top:278px}
.contact-heading{font-size:26px;color:var(--pale);font-weight:700;letter-spacing:.5px;opacity:.85}
.contact-list{list-style:none;position:absolute;left:76px;top:38px;width:180px}
.contact-list li{display:flex;align-items:center;gap:4px;color:var(--blue);font-size:5px;line-height:8px}
.contact-list li.phone{font-size:8px;line-height:11px}
.contact-list svg{width:5px;height:5px;flex:none}
</style>
</head>
<body>

<!-- Spread 1: back cover + front cover -->
<section class="spread spread-cover">
  <svg width="580" height="375" viewBox="0 0 580 375" style="position:absolute;left:0;top:0">
    <defs>
      <linearGradient id="skyFade" x1="0" y1="0" x2="0" y2="1">
        <stop offset="0" stop-color="#b9d1e3"/>
        <stop offset=".55" stop-color="#dfeaf3"/>
        <stop offset=".8" stop-color="#ffffff"/>
      </linearGradient>
      <linearGradient id="panelField" x1="0" y1="0" x2="1" y2="1">
        <stop offset="0" stop-color="#9fb2c6"/>
        <stop offset=".5" stop-color="#c4cfdb"/>
        <stop offset="1" stop-color="#6e6a5e"/>
      </linearGradient>
    </defs>
    <rect x="0" y="0" width="300" height="375" fill="url(#skyFade)" role="img" aria-label="Sky with wind turbine, soft motion blur"/>
    <rect x="290" y="55" width="290" height="320" fill="url(#panelField)" role="img" aria-label="Row of solar panels in a field under a cloudy sky"/>
    <rect x="290" y="0" width="290" height="55" fill="#ffffff"/>
    <path d="M580,116 H300 C252,116 252,172 300,180 C338,187 338,245 290,245 H0" fill="none" stroke="#0054AA" stroke-width="63"/>
  </svg>
  <div class="brand cover-brand-top">Kelvora Energy</div>
  <div class="cover-headline">
    <h1>YOUR RENEWABLE<br>ENERGY PARTNER</h1>
    <p>Comprehensive and Effective Renewable Energy Systems</p>
  </div>
  <div class="brand cover-brand-band">Kelvora Energy</div>
  <div class="contact">
    <div class="contact-heading">CONTACT US</div>
    <ul class="contact-list">
      <li><svg viewBox="0 0 10 10"><path d="M5 0a3.5 3.5 0 0 0-3.5 3.5C1.5 6 5 10 5 10s3.5-4 3.5-6.5A3.5 3.5 0 0 0 5 0z" fill="#5bb947"/></svg>4810 Orchard Ln Riverbend, CA 95000</li>
      <li class="phone"><svg viewBox="0 0 10 10"><path d="M2 0l2 2-1 1.5c.8 1.6 1.9 2.7 3.5 3.5L8 6l2 2-1.5 2C4 9.5.5 6 0 1.5z" fill="#5bb947"/></svg>209-555-0142</li>
      <li><svg viewBox="0 0 10 10"><circle cx="5" cy="5" r="4.5" fill="#5bb947"/></svg>sales@kelvoraenergy.com</li>
      <li><svg viewBox="0 0 10 10"><circle cx="5" cy="5" r="4.5" fill="#5bb947"/></svg>www.kelvoraenergy.com/</li>
    </ul>
  </div>
</section>

<!-- Spread 2: Solar + Storage -->
<section class="spread spread-solar">
  <div class="page page-left">
    <div class="wash" style="height:213px"></div>
    <h2 class="title">Solar Solutions</h2>
    <p class="sub" style="top:29px">Your business deserves a stress-free, simple, and secure experience</p>
    <div class="tab" style="left:0;top:88px;width:17px;height:100px"></div>
    <div class="photo" role="img" aria-label="Technician in hard hat with tablet beside solar panels on grass" style="left:17px;top:44px;width:273px;height:170px;background:linear-gradient(120deg,#2f5a9c,#7b9fd0 45%,#8fbf6a 75%,#4f8a3a)"></div>
    <div class="col" style="left:14px;top:226px">
      <h3>Increase Business Equity</h3>
      <p>Many studies prove that solar panels can be more valuable and increase the property value of homes and commercial buildings than those that don't, and that trend is unlikely to change anytime soon.</p>
      <p>The commercial solar revolution is becoming increasingly popular and adding solar panels to your building will make it more desirable.</p>
    </div>
    <div class="col" style="left:104px;top:226px">
      <h3>Improve Economics</h3>
      <p>Solar can reduce your overall operating cost by as much as 30%.</p>
      <p>Kelvora Energy helps businesses maximize solar savings so you can reinvest in, grow, and differentiate your business.</p>
      <p>Most businesses can go solar with no out-of-pocket expense and cash flow year one by taking advantage of tax credits and our expertise.</p>
    </div>
    <div class="col" style="left:194px;top:226px">
      <h3>Environmental Impact</h3>
      <p>It's no secret that solar lessens your reliance on other forms of energy and reduces your carbon footprint.</p>
      <p>A big benefit of solar panels for businesses is that they can build trust among your customers by demonstrating your commitment to sustainable energy and the environment.</p>
    </div>
    <div class="badge" style="left:4px;top:323px"><i></i>Serving all of Northern California - and beyond</div>
    <div class="badge" style="left:86px;top:323px"><i></i>Licensed and bonded in general structural contracting, electrical contracting and roofing contracting</div>
    <div class="badge" style="left:170px;top:323px"><i></i>High quality resources made in the USA</div>
    <div class="badge" style="left:230px;top:323px"><i></i>Customer support is our top priority</div>
  </div>
  <div class="page page-right">
    <div class="wash" style="height:300px"></div>
    <h2 class="title">Storage Solutions</h2>
    <p class="sub" style="top:29px">You will experience an easy, to-the-point process while being<br>guided by a highly trusted and experienced team.</p>
    <p class="lead" style="left:15px;top:63px">Consider us your long-term energy partners.</p>
    <ul class="checks" style="left:15px;top:78px;width:100px">
      <li>Corrective and Scheduled Maintenance</li>
      <li>Condition-based Maintenance</li>
      <li>Performance Optimization</li>
      <li>24/7 System Monitoring</li>
    </ul>
    <ul class="checks" style="left:118px;top:78px;width:120px">
      <li>Regular Site Visits</li>
      <li>Automated Cleaning Solutions</li>
      <li>Remote Diagnostics &amp; Power Operation</li>
      <li>48 Hour Emergency Response</li>
    </ul>
    <div class="photo" role="img" aria-label="Building with rooftop solar panels and wind turbines on a green lawn" style="left:0;top:124px;width:274px;height:140px;background:linear-gradient(180deg,#dbe8f3 0%,#b7d0e6 45%,#5c6a78 62%,#6fa54a 75%,#4e8a34)"></div>
    <div class="tab" style="left:274px;top:165px;width:16px;height:85px"></div>
    <div class="col" style="left:10px;top:308px;width:80px">
      <h3>Protect your energy assets</h3>
      <p>With your maintenance plan, you can be assured that your investment is kept in good shape and producing 100%. This consistency in production over time ensures a positive return on investment.</p>
    </div>
    <div class="col" style="left:98px;top:308px;width:86px">
      <h3>Maintain energy savings</h3>
      <p>It is crucial to keep an energy-efficient solar system maintained after installation and to optimize it to offer maximum savings.</p>
      <p>There are many things we can do to assure your system operates at the highest efficiency, such as regular cleaning, performance monitoring, removing debris, etc.</p>
    </div>
    <div class="col" style="left:192px;top:308px;width:86px">
      <h3>Focus on your business</h3>
      <p>Managing your energy systems is not your primary function when you're an owner or manager.</p>
      <p>You can trust us to take care of your energy systems, saving you money and time and allowing you more time to grow and manage your business.</p>
    </div>
  </div>
</section>

<!-- Spread 3: O&M + Cleaning -->
<section class="spread spread-om">
  <div class="page page-left">
    <div class="wash" style="height:172px"></div>
    <h2 class="title">O&amp;M Solution</h2>
    <div class="tab" style="left:0;top:60px;width:17px;height:90px"></div>
    <div class="photo" role="img" aria-label="Crew in safety vests servicing rooftop solar panels" style="left:17px;top:35px;width:198px;height:137px;background:linear-gradient(180deg,#4f7a3e 0%,#6d8f55 35%,#8ea6c4 50%,#6f8fb8 80%,#c7ccd3)"></div>
    <p class="body" style="position:absolute;left:221px;top:33px;width:64px;font-size:4.5px;line-height:5.6px">A well maintained solar PV system can perform up to 30% better than one which is not? Components within your solar PV system could be void of all warranties if routine maintenance is not performed? Without third party verification of your system, poorly installed components could forever go unnoticed?</p>
    <div class="col" style="left:16px;top:182px;width:126px">
      <p class="subhead">The Truth</p>
      <p>Similar to conventional electrical power generation assets, solar PV systems encounter operational hurdles that will disrupt performance and hurt annual revenues. Even with proper manufacturing and installation, systems face extreme weather, module soiling, communication errors, loose terminations, ground faults, rodents, vandalism, heat expansion and vibration that can damage or destroy equipment.</p>
    </div>
    <div class="col" style="left:150px;top:182px;width:126px">
      <p class="subhead">The Solution</p>
      <p>Kelvora Energy's solar service plans are designed to shield and protect solar PV investments from unavoidable degradation. We understand the fiscal importance of keeping your solar PV system operating at optimal performance. Our cost-effective and proactive approach goes beyond the standard "when it breaks, we will fix it" approach.</p>
    </div>
    <div class="col" style="left:16px;top:256px;width:262px">
      <p class="subhead">Shield &amp; protect your solar power investments</p>
      <p><b>Bronze Shield:</b><br>The inverter is the heart of your solar PV system. Our factory trained technicians perform preventative maintenance with visual inspections of the arrays and combiner boxes, plus access to our Customer Support hotline and a yearly maintenance summary report.</p>
      <p><b>Silver Shield:</b><br>The most cost-effective way to prevent degradation is proactive performance monitoring. Silver adds real-time monitoring, alarm triage, thermal imaging scans of DC wiring and inverters, and quarterly performance reports.</p>
      <p><b>Gold Shield:</b><br>Our most complete plan. Gold adds annual performance testing and verification, calibration, emergency dispatch within 24 hours, warranty compliance and spare parts inventory management.</p>
    </div>
  </div>
  <div class="page page-right">
    <div class="wash" style="height:290px"></div>
    <h2 class="title">Cleaning Solution</h2>
    <p class="sub" style="top:29px">The system uses two separate water filter technologies to ensure only the cleanest water is used.<br>This helps to prevent harmful water scaling and corrosion!</p>
    <div class="col" style="left:15px;top:52px;width:76px">
      <p class="subhead">Automatic nightly cleaning</p>
      <p>The system cleans regularly, at night, keeping the panels consistently clean preventing dirt and limescale buildup – thus increasing energy production by upwards of 30%.</p>
      <p class="subhead" style="margin-top:6px">Safe &amp; efficient</p>
      <p>The system distributes water through an automated, reliable system – reducing labor, safety hazards and damage to rooftops. No chemicals or abrasive brushes are used, helping the system achieve the lowest operating costs possible.</p>
      <p class="subhead" style="margin-top:6px">Warranty compliant</p>
      <p>The system cleans the panels at night to avoid thermal stress to the module glass. By keeping the modules clean with no abrasive brushes, you can ensure warranty compliance with your module manufacturer.</p>
    </div>
    <div class="photo" role="img" aria-label="Close-up of a water spray nozzle cleaning a solar panel" style="left:108px;top:72px;width:166px;height:200px;background:linear-gradient(160deg,#e9eef3 0%,#9fb0c2 35%,#4f5d6b 65%,#1f2730)"></div>
    <div class="tab" style="left:274px;top:110px;width:16px;height:120px"></div>
    <p class="lead" style="left:15px;top:304px;width:110px;font-size:5.4px;line-height:6.6px">Consider us your long-term energy partners.</p>
    <ul class="checks" style="left:15px;top:324px;width:66px">
      <li>Increase Production</li>
      <li>Robust Technology</li>
      <li>Remotely Controlled</li>
    </ul>
    <ul class="checks" style="left:85px;top:324px;width:100px">
      <li>Safer Cleaning</li>
      <li>Protects Solar Panel Warranty</li>
      <li>Proven Technology</li>
    </ul>
  </div>
</section>

<!-- Spread 4: Electrical + Roofing -->
<section class="spread spread-trades">
  <div class="page page-left">
    <div class="wash" style="height:200px"></div>
    <h2 class="title" style="font-size:14px;line-height:14.5px">Electricians that can<br>handle any job</h2>
    <p class="sub" style="top:44px">Electrical work can having shocking outcomes if you don't have the right Contractor.</p>
    <div class="tab" style="left:0;top:70px;width:17px;height:95px"></div>
    <div class="photo" role="img" aria-label="Electrician in a bucket lift working on overhead lines above a street" style="left:17px;top:58px;width:256px;height:136px;background:linear-gradient(180deg,#6c8a5a 0%,#8a9a86 40%,#a7adb3 60%,#5d7b4a)"></div>
    <p class="lead" style="left:15px;top:204px;width:262px">Kelvora Energy is a fully licensed and experienced electrical contractor.</p>
    <p class="body" style="position:absolute;left:15px;top:222px;width:240px;font-size:5px;line-height:6px">Whether you just need some additional lights or a whole new system, our team stands ready to perform from concept to completion.</p>
    <p class="subhead" style="position:absolute;left:15px;top:262px">Electrical</p>
    <ul class="checks wide" style="left:15px;top:276px;width:190px">
      <li>Integrating your energy efficiency plan to include a electrical switch gear, new transformers, AC upgrades, LED lighting is also an excellent way to improve your carbon footprint.</li>
      <li>Kelvora will evaluate and design everything you need to fully integrate every aspect of your electrical system with your Renewable Energy goals.</li>
      <li>Not looking to go Green? No problem. We handle every aspect of conventional electrical work as well.</li>
    </ul>
  </div>
  <div class="page page-right">
    <div class="wash" style="height:262px"></div>
    <h2 class="title" style="font-size:14px;line-height:14.5px">Energy efficient roofing<br>done right</h2>
    <p class="sub" style="top:44px">Enhance quality, and decrease overall costs by combining services</p>
    <p class="lead" style="left:15px;top:60px;width:240px;font-size:7px;line-height:8.6px">Increase savings and improve quality by using one contractor for all of your businesses energy efficient needs.</p>
    <p class="body" style="position:absolute;left:15px;top:90px;width:230px;font-size:4.8px;line-height:5.8px">We will help you choose from a variety of roofing options including: TPO, Silicon, Standing Seam, and all with a 20 year warranty!</p>
    <div class="photo" role="img" aria-label="Aerial view of a white flat commercial roof with trees beyond" style="left:0;top:126px;width:274px;height:130px;background:linear-gradient(180deg,#cfe0ee 0%,#9fb7cc 25%,#4f6f55 35%,#e5e9ec 55%,#f4f6f8)"></div>
    <div class="tab" style="left:274px;top:160px;width:16px;height:80px"></div>
    <p class="subhead" style="position:absolute;left:15px;top:303px">Energy efficient roofing</p>
    <ul class="checks wide" style="left:15px;top:317px;width:215px">
      <li>Integrating your energy efficiency plan to include a "cool roof" is an extremely intelligent strategy. Whether you require a new roof, or a roof restoration Kelvora Energy will get you to success with minimal construction time, and the highest quality workmanship guaranteed.</li>
      <li>Don't want to upgrade to the latest Title 24 Standards? We can help get you into brand new roof without subjecting your existing building to new building standards.</li>
    </ul>
  </div>
</section>

</body>
</html>
```